Web landing page design

- Create a Web Design (Uncoded - PSD layout only)

We need a single web page design to promote our service. This page will
acts as a landing page for users and also be utilized in social media
advertising. Please provide us with a cutting edge design. I have attached
a link for what the company is about. In essence we are a photo checking
service which reviews photos for retailers, hotels abd car dealerships to
check everything is good after a service has been performed. Whether it be
a new promotion, cleaning or just checking prices. I am looking for a
design to say that we do many photos and at a very cost effective price
(team based in Mexico)

Link: https://slidora.example/view/kq3Fz8wPnT2dXr7HsLmV/
*Deadline*
5 days
*Updates*

- The Start Here box needs to look like this:

-Start Here (heading)
-A box for email addresses to be entered
-Then a check box with "Yes, I have read and agree to the Privacy Policy
and agree to receive email marketing from Tallumo38'
-A submit button

All of this information needs to be in one box please. And please feel
free to contact me if you have any questions about this.

*Target Market(s)*
Retail business, Merchandising companies, Rental property owners, Car
dealers
Updates

Please can you submit entries. I am just looking for a tidy to a presentation already created. Just needs design touches.

Target Market(s)

Ability for audience to understand concept quickly
Benefits to why to use the product stand out
Technology driven approach

Industry/Entity Type

Retail

Number of Pages Required

1 page

Colors
0792cd

Requirements
Must have
• Clean and modern design

```html
<!DOCTYPE html>
<html lang="en">
<head>
<meta charset="utf-8">
<title>Clarivo – Start Here</title>
<link href="https://fonts.googleapis.com/css2?family=Lato:wght@300;400;700&display=swap" rel="stylesheet">
<style>
  :root {
    --brand: #0792cd;
    --brand-deep: #1a7fc4;
    --ink: #333a40;
    --white: #ffffff;
    --rule: #d4d8dc;
    --hero-dark: #1b2630;
    --hero-mid: #3b4d5c;
    --hero-warm: #6b5548;
  }
  * { box-sizing: border-box; margin: 0; padding: 0; }
  html, body { width: 1200px; height: 844px; overflow: hidden; }
  body { font-family: "Lato", sans-serif; background: var(--white); position: relative; }

  .hero { position: absolute; left: 0; top: 0; width: 1200px; height: 633px; overflow: hidden; }
  .hero-photo {
    position: absolute; inset: 0;
    background:
      radial-gradient(ellipse 300px 360px at 820px 220px, rgba(150,110,90,.55), transparent 70%),
      radial-gradient(ellipse 320px 420px at 200px 220px, rgba(140,160,180,.55), transparent 70%),
      linear-gradient(180deg, var(--hero-mid) 0%, var(--hero-dark) 100%);
  }
  .hero-photo::after { content: ""; position: absolute; inset: 0; background: rgba(10,20,30,.25); }

  .site-header { position: absolute; top: 0; left: 0; right: 0; height: 100px; }
  .brand { position: absolute; left: 116px; top: 26px; display: flex; align-items: center; gap: 10px; }
  .brand-dot { width: 46px; height: 46px; border-radius: 50%; background: var(--brand); }
  .brand-name { color: var(--white); font-size: 38px; font-weight: 400; letter-spacing: .5px; }
  .main-nav a {
    position: absolute; top: 38px; color: var(--white); text-decoration: none;
    font-size: 19px; font-weight: 400;
  }

  .signup { position: absolute; left: 0; top: 238px; width: 1200px; }
  .signup-title {
    position: absolute; left: 0; width: 1180px; text-align: center; top: 0;
    color: var(--white); font-size: 62px; font-weight: 700; letter-spacing: .5px;
  }
  .email-frame {
    position: absolute; left: 256px; top: 82px; width: 657px; height: 74px;
    border: 1.5px solid rgba(255,255,255,.55); border-radius: 37px;
  }
  .email-field {
    position: absolute; left: 8px; top: 7px; width: 640px; height: 58px;
    border-radius: 29px; border: none;
    background: linear-gradient(180deg, #ffffff 0%, #e9eaeb 100%);
    padding-left: 33px; font-family: "Lato", sans-serif; font-size: 18px; color: #555;
  }
  .email-field::placeholder { color: #555; }
  .consent { position: absolute; left: 252px; top: 168px; display: flex; align-items: center; gap: 9px; }
  .consent-box { width: 20px; height: 20px; background: #f2f2f2; border: 1px solid #ccc; appearance: none; }
  .consent-text { color: var(--white); font-size: 14.6px; }
  .submit-btn {
    position: absolute; left: 525px; top: 204px; width: 146px; height: 48px;
    border: none; border-radius: 24px; background: var(--brand-deep); color: var(--white);
    font-family: "Lato", sans-serif; font-size: 22px;
  }

  .stats { position: absolute; left: 0; top: 633px; width: 1200px; height: 138px; background: var(--white); }
  .stat { position: absolute; top: 0; height: 138px; text-align: center; }
  .stat + .stat { border-left: 1px solid var(--rule); }
  .stat-value { display: block; margin-top: 30px; color: var(--brand-deep); font-size: 41px; font-weight: 400; line-height: 1; }
  .stat-label { display: block; margin-top: 16px; color: var(--ink); font-size: 13.5px; line-height: 20px; text-transform: uppercase; }

  .site-footer { position: absolute; left: 0; top: 771px; width: 1200px; height: 73px; background: var(--brand-deep); }
  .legal { position: absolute; left: 138px; top: 24px; color: var(--white); font-size: 14px; font-weight: 300; }
  .social { position: absolute; left: 938px; top: 17px; display: flex; gap: 5px; }
  .social span { width: 32px; height: 32px; border-radius: 50%; border: 1.5px solid var(--white); }
</style>
</head>
<body>
  <section class="hero">
    <div class="hero-photo" role="img" aria-label="Smiling retail assistant holding a tablet in a clothing store, shirts on rails behind her"></div>

    <header class="site-header">
      <div class="brand">
        <span class="brand-dot"></span>
        <span class="brand-name">Clarivo</span>
      </div>
      <nav class="main-nav">
        <a href="#" style="left:631px">About</a>
        <a href="#" style="left:743px">Results</a>
        <a href="#" style="left:865px">How</a>
        <a href="#" style="left:964px">Free Trial</a>
      </nav>
    </header>

    <form class="signup">
      <h1 class="signup-title">Start Here</h1>
      <div class="email-frame">
        <input class="email-field" type="email" placeholder="Your Email address">
      </div>
      <label class="consent">
        <input class="consent-box" type="checkbox">
        <span class="consent-text">Yes, I have read and agree to the Privacy Policy and agree to receive email marketing from Tallumo38</span>
      </label>
      <button class="submit-btn" type="submit">Submit</button>
    </form>
  </section>

  <section class="stats">
    <div class="stat" style="left:150px;width:225px"><span class="stat-value">2.2m</span><span class="stat-label">Photos reviewed<br>last year</span></div>
    <div class="stat" style="left:375px;width:216px"><span class="stat-value">5p</span><span class="stat-label">From per photo<br>reviewed</span></div>
    <div class="stat" style="left:591px;width:247px"><span class="stat-value">97.2%</span><span class="stat-label">Average<br>compliance</span></div>
    <div class="stat" style="left:838px;width:230px"><span class="stat-value">3-8%</span><span class="stat-label">Sales<br>increase</span></div>
  </section>

  <footer class="site-footer">
    <p class="legal">© 2018 Company Name &nbsp;All right reserved &nbsp;Terms of Use</p>
    <div class="social"><span></span><span></span><span></span><span></span></div>
  </footer>
</body>
</html>
```